Non-Profit, Organic, Natural Feel, Clean & Simple Business Cards

Looking for a business card design. Has an organic, natural, new-age, clean and simple look/feel. We are a non-profit group that works with Moringa(a health plant/superfood) by spreading and sharing seeds of Moringa. A design that stands out but clean and professional. I will upload our new logo design. The font can be changed. Also I will upload some pictures of Moringa.
Our Facebook page is www.socialvine.com/TavelliCircle Check us out to get a feel of us.

Target Market(s)

Everyone. Movers & Shakers of The Sustainable, Natural Medicines & Cosmetics, Organic Food Farming Industry. And To The Common Person Or A Local Family.

Industry/Entity Type

Sustainability

Contact Information for Business Card

Email: TavelliSoilCircle@Postvane.com
FB: www.Socialvine.com/TavelliCircle
Website: www.TavelliCircle.com

Requirements
Must have
• Image/Pic/Design of Moringa Leaves. Somewhere on the card. Clean and Clear. So you could easily identify the Moringa from the Business Card. Something Alive, Living, Green Feel to the card design.
Nice to have
• A warm, friendly, professional feel to the design. A organic sustainable concept/future with Moringa is the business card impression/image we are trying to present.

```html
<!DOCTYPE html>
<html lang="en">
<head>
<meta charset="utf-8">
<title>Tavelli Circle – Business Cards</title>
<link rel="stylesheet" href="https://fonts.googleapis.com/css2?family=Arvo&display=swap">
<style>
  :root {
    --page: #e3e3e3;
    --card-white: #ffffff;
    --leaf-pale: #eef3ea;
    --leaf-pale-deep: #e2ebdc;
    --green: #6db31c;
    --green-deep: #5aa70c;
    --green-tab: #5fa80a;
    --brand-grey: #8b8f7c;
    --ink: #0b0b0b;
  }
  * { box-sizing: border-box; margin: 0; padding: 0; }
  html, body {
    width: 1200px;
    height: 900px;
    overflow: hidden;
    background: var(--page);
    font-family: "Arvo", Georgia, serif;
  }
  .card {
    position: absolute;
    left: 336px;
    width: 517px;
    height: 293px;
    overflow: hidden;
  }
  .card--front { top: 152px; background: var(--card-white); }
  .card--back  { top: 476px; background: var(--green); }

  .leaf-field {
    position: absolute;
    inset: 0;
  }
  .card--front .leaf-field {
    background:
      radial-gradient(ellipse 38% 42% at 70% 30%, var(--leaf-pale-deep), transparent 70%),
      radial-gradient(ellipse 35% 40% at 40% 82%, var(--leaf-pale), transparent 70%),
      radial-gradient(ellipse 30% 35% at 88% 80%, var(--leaf-pale), transparent 70%);
  }
  .card--back .leaf-field {
    background:
      radial-gradient(ellipse 40% 40% at 65% 22%, var(--green-deep), transparent 72%),
      radial-gradient(ellipse 38% 40% at 35% 78%, var(--green-deep), transparent 72%),
      radial-gradient(ellipse 30% 35% at 85% 75%, var(--green-deep), transparent 72%);
  }

  .side-tab {
    position: absolute;
    top: 59px;
    width: 10px;
    height: 176px;
    border-radius: 2px;
  }
  .side-tab--left  { left: 0; }
  .side-tab--right { right: 0; }
  .card--front .side-tab { background: var(--green-tab); }
  .card--back .side-tab  { background: var(--ink); }

  .brand {
    position: absolute;
    left: 31px;
    top: 92px;
    display: flex;
    align-items: center;
    gap: 18px;
    color: var(--brand-grey);
  }
  .brand-square {
    width: 90px;
    height: 112px;
    background: var(--green);
    border-radius: 3px;
  }
  .brand-name { display: flex; flex-direction: column; align-items: center; }
  .brand-name__main {
    font-size: 50px;
    line-height: 1;
    letter-spacing: 1px;
  }
  .brand-name__sub {
    margin-top: 8px;
    font-size: 26px;
    letter-spacing: 20px;
    margin-right: -20px;
  }

  .contact {
    position: absolute;
    left: 0;
    right: 0;
    top: 89px;
    text-align: center;
    color: var(--ink);
  }
  .contact__name {
    font-size: 25px;
    font-weight: 400;
    margin-bottom: 8px;
  }
  .contact__line {
    font-size: 17px;
    line-height: 28px;
  }
</style>
</head>
<body>
  <section class="card card--front">
    <div class="leaf-field" role="img" aria-label="Faint photograph of moringa leaves on a branch"></div>
    <span class="side-tab side-tab--left"></span>
    <span class="side-tab side-tab--right"></span>
    <div class="brand">
      <span class="brand-square"></span>
      <div class="brand-name">
        <span class="brand-name__main">TAVELLI</span>
        <span class="brand-name__sub">CIRCLE</span>
      </div>
    </div>
  </section>

  <section class="card card--back">
    <div class="leaf-field" role="img" aria-label="Green-tinted photograph of moringa leaves"></div>
    <span class="side-tab side-tab--left"></span>
    <span class="side-tab side-tab--right"></span>
    <div class="contact">
      <h1 class="contact__name">TAVELLI CIRCLE</h1>
      <p class="contact__line">Email: TavelliSoilCircle@Postvane.com</p>
      <p class="contact__line">FB: www.Socialvine.com/TavelliCircle</p>
      <p class="contact__line">Website: www.TavelliCircle.com</p>
    </div>
  </section>
</body>
</html>
```